Website needed for a specialty chemical company!

We are looking for a new website design to replace our current site.
We are a woman and minority owned, specialty chemical company that specializes in environmentally safe products and chemicals, or what we like to call "green solutions".
Our clientele are mostly companies in the construction business, as our current products consist of asphalt release agents, tar/asphalt cleaners, concrete form release agents, concrete removers and environmentally safe detergents. If a special product is needed, our formulation team can also custom create chemicals and products for your industry or company.
We are looking for at least three pages total. A home page, a products page that lists our products and also provides additional product information and a contact us page.
Our current site is at: www.brovalin-solvex.com
This will give you a general idea of what type of content will be on our site.
We are very open to content ideas, pictures, colors and CREATIVITY.
We would like to stress that we are "environmentally friendly" and would like to use "earthy" tones and greens if possible.
We also prefer a more modern website design as opposed to something traditional. An example of a site design that we like is: http://www.tarivo.com/
The design does not have to follow this, this is just a site look and feel that we liked. :)
Updates
Target Market(s)
Construction Companies, Truckers
Industry/Entity Type
It Company
Coding
Coded - Design and coding required
Number of Pages Required
3 page
Font styles to use
Look and feel
Each slider illustrates characteristics of the customer's brand and the style your logo design should communicate.

```html
<!DOCTYPE html>
<html lang="en">
<head>
<meta charset="utf-8">
<title>Brovalin Solvex — Green Solutions</title>
<link rel="stylesheet" href="https://fonts.googleapis.com/css2?family=Catamaran:wght@400;500;600;700&family=Open+Sans:wght@400;600&display=swap">
<style>
:root{
  --green:#2f9a5e;
  --green-dark:#1f7d47;
  --green-deep:#178047;
  --band-top:#7cb842;
  --band-bottom:#16854a;
  --ink:#333;
  --muted:#8a8a8a;
  --footer:#2c2c2c;
  --footer-bottom:#1e1e1e;
  --white:#fff;
}
*{box-sizing:border-box;margin:0;padding:0}
html,body{width:1200px;height:2362px;overflow:hidden;background:#fff}
body{position:relative;font-family:"Catamaran",sans-serif;color:var(--ink)}
.abs{position:absolute}

/* header */
.topbar{left:0;top:0;width:1200px;height:90px;background:var(--green)}
.brand{left:47px;top:0;width:229px;height:189px;background:#fff;display:flex;flex-direction:column;justify-content:center;align-items:center;gap:0}
.brand span{font-family:"Catamaran",sans-serif;font-weight:700;color:var(--green-deep);font-size:34px;line-height:36px;letter-spacing:1px}
.nav a{position:absolute;top:35px;height:30px;line-height:30px;font-family:"Open Sans",sans-serif;font-size:11px;color:#1c5a34;text-decoration:none;text-transform:uppercase}
.nav .active{border:1px solid #fff;color:#fff;padding:0 17px}
.login{left:828px;top:32px;width:101px;height:33px;background:#4fb57d;color:#fff;font-family:"Open Sans",sans-serif;font-size:14px;line-height:33px;text-align:center}
.ico{top:33px;width:32px;height:32px;border:2px solid #fff;border-radius:50%;display:flex;align-items:center;justify-content:center}
.cart-count{left:1102px;top:40px;color:#fff;font-family:"Open Sans",sans-serif;font-size:12px}

/* hero */
.hero{left:0;top:190px;width:1200px;height:566px;background:linear-gradient(180deg,#9cc6e6 0%,#cfe4f1 40%,#a8cf6a 72%,#4f8e24 100%)}
.hero-panel{left:633px;top:328px;width:520px;height:256px;background:rgba(90,100,100,.72);padding:22px 30px;text-align:right;color:#fff}
.hero-panel h1{font-size:35px;font-weight:700;line-height:44px;margin-bottom:8px}
.hero-panel p{font-family:"Open Sans",sans-serif;font-size:13px;line-height:23px;padding-left:60px}
.btn-light{left:387px;top:155px;width:103px;height:38px;background:#fff;color:var(--green);font-family:"Open Sans",sans-serif;font-size:13px;line-height:38px;text-align:center}
.dots{left:186px;top:215px;display:flex;gap:6px}
.dots i{width:9px;height:9px;border-radius:50%;background:#fff}
.dots i.on{background:var(--green)}

/* section headings */
.rule{height:1px;background:#bbb}
.heading{left:0;width:1200px;text-align:center;font-size:36px;font-weight:700;color:var(--green-deep);letter-spacing:1px}

/* features */
.feature{top:861px;width:342px;height:273px;text-align:center}
.feature.boxed{border:2px solid #ddd;box-shadow:0 0 4px rgba(0,0,0,.1)}
.feature .icon{width:66px;height:66px;margin:16px auto 0;display:flex;align-items:center;justify-content:center}
.feature h3{font-size:25px;font-weight:500;margin-top:20px;line-height:30px}
.feature p{font-family:"Open Sans",sans-serif;font-size:12px;line-height:17px;color:var(--muted);margin:12px auto 0;width:300px}
.feature .more{display:inline-block;margin-top:16px;width:102px;height:34px;line-height:32px;border:1.5px solid var(--green);color:var(--green-deep);font-family:"Open Sans",sans-serif;font-size:11px;font-weight:600}
.feature.boxed h3{color:#333}
.feature.boxed .more{border-color:#333;color:#333}
.feature h3.g{color:var(--green-deep)}

/* products */
.tile{width:544px;height:270px;color:#fff;text-align:center}
.tile h4{position:absolute;left:0;right:0;top:86px;font-size:25px;font-weight:600;letter-spacing:1px}
.tile .line{position:absolute;left:112px;width:320px;top:124px;height:1px;background:rgba(255,255,255,.6)}
.tile p{position:absolute;left:40px;right:40px;top:131px;font-family:"Open Sans",sans-serif;font-size:12.5px;font-weight:600;line-height:16px}
.tile .cta{position:absolute;left:218px;top:177px;width:123px;height:34px;border:1px solid #fff;font-family:"Open Sans",sans-serif;font-size:13px;line-height:32px}
.tile .cta.fill{background:var(--green-dark);border-color:var(--green-dark)}

/* green band */
.band{left:0;top:1838px;width:1200px;height:273px;background:linear-gradient(180deg,var(--band-top),var(--band-bottom));color:#fff}
.band h5{font-size:19px;font-weight:500;position:absolute;top:24px}
.band p{font-family:"Open Sans",sans-serif;font-size:12px;line-height:16px;position:absolute}
.band .outline{position:absolute;left:55px;top:208px;width:126px;height:38px;border:1px solid #fff;font-family:"Open Sans",sans-serif;font-size:13px;line-height:36px;text-align:center}
.email{left:427px;top:130px;width:296px;height:36px;background:#fff;color:#aaa;font-family:"Open Sans",sans-serif;font-size:11px;line-height:36px;padding-left:12px}
.subscribe{left:427px;top:176px;width:296px;height:36px;background:#444;color:#fff;font-family:"Open Sans",sans-serif;font-size:13px;line-height:36px;text-align:center}
.map{left:797px;top:80px;width:353px;height:161px;background:linear-gradient(135deg,#e9e6dc,#d6dfc8 60%,#cdd9e6)}

/* footer */
.footer{left:0;top:2111px;width:1200px;height:193px;background:var(--footer);color:#fff}
.footer h6{position:absolute;top:36px;font-size:16px;font-weight:500;letter-spacing:.3px}
.footer .col{position:absolute;top:68px;font-family:"Open Sans",sans-serif;font-size:11.5px;line-height:22px;color:#ddd}
.footer .sep{position:absolute;top:32px;width:1px;height:126px;background:#444}
.footer li{list-style:none;padding-left:14px;position:relative}
.footer li::before{content:"›";position:absolute;left:0;color:#aaa}
.contact div{display:flex;gap:10px;align-items:flex-start}
.contact svg{flex:none;margin-top:5px}
.bottom{left:0;top:2304px;width:1200px;height:58px;background:var(--footer-bottom);color:#777;font-family:"Open Sans",sans-serif;font-size:10px;text-align:center;line-height:58px}
.social{top:2314px;width:28px;height:28px}
</style>
</head>
<body>

<header>
  <div class="abs topbar"></div>
  <div class="abs brand"><span>BROVALIN</span><span>SOLVEX</span></div>
  <nav class="nav">
    <a class="active" style="left:310px">Home</a>
    <a style="left:414px">Products</a>
    <a style="left:527px">Contact Us</a>
    <a style="left:650px">My Account</a>
  </nav>
  <div class="abs login">LOGIN</div>
  <div class="abs ico" style="left:941px"><svg width="12" height="16" viewBox="0 0 12 16"><path d="M6 0a6 6 0 0 0-6 6c0 4.5 6 10 6 10s6-5.5 6-10a6 6 0 0 0-6-6zm0 8.5A2.5 2.5 0 1 1 6 3.5a2.5 2.5 0 0 1 0 5z" fill="#fff"/></svg></div>
  <div class="abs ico" style="left:984px"><svg width="14" height="14" viewBox="0 0 14 14"><path d="M3 1l2.5 3-1.5 1.5c.8 1.8 2.2 3.2 4 4L9.5 8 13 10.5 11.5 13C6 13 1 8 1 2.5z" fill="#fff"/></svg></div>
  <div class="abs ico" style="left:1024px"><svg width="14" height="14" viewBox="0 0 14 14"><circle cx="6" cy="6" r="4.2" stroke="#fff" stroke-width="2" fill="none"/><path d="M9 9l4 4" stroke="#fff" stroke-width="2"/></svg></div>
  <div class="abs ico" style="left:1063px"><svg width="16" height="14" viewBox="0 0 16 14"><path d="M0 1h3l2 8h9l2-6H4.5" stroke="#fff" stroke-width="1.6" fill="none"/><circle cx="6" cy="12" r="1.4" fill="#fff"/><circle cx="13" cy="12" r="1.4" fill="#fff"/></svg></div>
  <div class="abs cart-count">: 0 item</div>
</header>

<section class="abs hero" role="img" aria-label="Close-up photo of fresh green grass blades against a bright blue sky"></section>
<div class="abs hero-panel">
  <h1>Welcome to Brovalin Solvex™</h1>
  <p>Brovalin Solvex™ offers environmentally friendly products made from all natural and renewable resources. Our products are safe, and easy to use.</p>
  <div class="abs btn-light">Read More</div>
  <div class="abs dots"><i></i><i class="on"></i><i></i><i></i></div>
</div>

<section class="why">
  <div class="abs rule" style="left:47px;top:819px;width:327px"></div>
  <div class="abs rule" style="left:826px;top:819px;width:327px"></div>
  <h2 class="abs heading" style="top:796px">WHY BROVALIN SOLVEX™?</h2>

  <div class="abs feature boxed" style="left:49px">
    <div class="icon" style="background:#3f3f3f">
      <svg width="36" height="36" viewBox="0 0 36 36"><circle cx="18" cy="12" r="7" fill="#5cb85c"/><path d="M6 34c0-8 5-13 12-13s12 5 12 13z" fill="#5cb85c"/><path d="M15 27c3-6 9-6 12-6-1 5-5 8-12 6z" fill="#fff"/></svg>
    </div>
    <h3>SAFE TO USE</h3>
    <p>Brovalin Solvex products contain no dangerous chemicals or additives and are safe around you, your family, your pets and the environment</p>
    <span class="more">READ MORE</span>
  </div>

  <div class="abs feature" style="left:427px">
    <div class="icon" style="background:var(--green)">
      <svg width="44" height="44" viewBox="0 0 44 44"><circle cx="22" cy="22" r="19" fill="none" stroke="#fff" stroke-width="3"/><circle cx="22" cy="22" r="12" fill="none" stroke="#fff" stroke-width="3"/><circle cx="22" cy="22" r="5" fill="#fff"/></svg>
    </div>
    <h3 class="g">EFFECTIVE</h3>
    <p>Brovalin Solvex products contain no dangerous chemicals or additives and are safe around you, your family, your pets and the environment</p>
    <span class="more">READ MORE</span>
  </div>

  <div class="abs feature" style="left:801px">
    <div class="icon" style="background:var(--green)">
      <svg width="30" height="44" viewBox="0 0 30 44"><text x="15" y="36" text-anchor="middle" fill="#fff" font-family="Catamaran,sans-serif" font-size="42" font-weight="700">$</text></svg>
    </div>
    <h3 class="g">ECONOMICALLY PRICED</h3>
    <p>Brovalin Solvex products contain no dangerous chemicals or additives and are safe around you, your family, your pets and the environment</p>
    <span class="more">READ MORE</span>
  </div>
</section>

<section class="products">
  <div class="abs rule" style="left:47px;top:1197px;width:391px"></div>
  <div class="abs rule" style="left:761px;top:1197px;width:392px"></div>
  <h2 class="abs heading" style="top:1174px">OUR PRODUCTS</h2>

  <div class="abs tile" style="left:47px;top:1254px;background:linear-gradient(160deg,#2f5a1f,#2d4a22 55%,#1c2a2a)" role="img" aria-label="Photo of a gloved hand sampling green plants in a lab">
    <h4>PORESORB™</h4><div class="line"></div>
    <p>The PoreSorb™ product line offers green solutions utilizing the benefits of the naturally occurring mineral, Zeolite.</p>
    <div class="cta">Read More &nbsp;▸</div>
  </div>
  <div class="abs tile" style="left:610px;top:1254px;background:linear-gradient(160deg,#5b6266,#3f4548 60%,#2c3033)" role="img" aria-label="Photo of a worker in a chemical production plant">
    <h4>CLEARLIFT™</h4><div class="line"></div>
    <p>The PoreSorb™ product line offers green solutions utilizing the benefits of the naturally occurring mineral, Zeolite.</p>
    <div class="cta fill">Read More &nbsp;▸</div>
  </div>
  <div class="abs tile" style="left:47px;top:1543px;background:linear-gradient(160deg,#6a6d6a,#3f4740 60%,#2f4a22)" role="img" aria-label="Photo of a worker in a protective suit handling plants">
    <h4>TARLIFT™</h4><div class="line"></div>
    <p>The PoreSorb™ product line offers green solutions utilizing the benefits of the naturally occurring mineral, Zeolite.</p>
    <div class="cta">Read More &nbsp;▸</div>
  </div>
  <div class="abs tile" style="left:610px;top:1543px;background:linear-gradient(160deg,#4d6a8a,#3d4a55 55%,#5a4a2a)" role="img" aria-label="Photo of an industrial refinery with an engineer holding a hard hat">
    <h4>FROSTLIFT™</h4><div class="line"></div>
    <p>The PoreSorb™ product line offers green solutions utilizing the benefits of the naturally occurring mineral, Zeolite.</p>
    <div class="cta">Read More &nbsp;▸</div>
  </div>
</section>

<section class="abs band">
  <h5 style="left:55px">CUSTOMIZED PRODUCT REQUESTS</h5>
  <p style="left:55px;top:80px;width:300px;text-align:justify">Brovalin Solvex™ offers customized product/formulation services. Our technical experts can collaborate with you to create on-target formulation for any of your chemical needs. If a chemical you need is not on our product list, contact the Brovalin Solvex™ Product Formulation Team and speak to one of our representatives.</p>
  <div class="outline">Read More</div>

  <h5 style="left:425px">NEWSLETTER SIGNUP</h5>
  <p style="left:425px;top:84px;width:300px">Subscribe our newsletter to know our daily updates and offer daily updates and offer</p>
  <div class="abs email">Enter your Email Id</div>
  <div class="abs subscribe">SUBSCRIBE</div>

  <h5 style="left:801px">LOCATION</h5>
  <div class="abs map" role="img" aria-label="Street map showing the office location"></div>
</section>

<footer class="abs footer">
  <h6 style="left:60px">ABOUT US</h6>
  <div class="col" style="left:60px;width:225px;line-height:16px;top:70px">Brovalin Solvex™ is a woman owned, minority business specializing in the manufacturing and distribution of environmentally safe chemicals</div>
  <div class="sep" style="left:330px"></div>

  <h6 style="left:397px">CUSTOMER SERVICES</h6>
  <ul class="col" style="left:402px"><li>Security &amp; Privacy</li><li>Payment Options</li><li>Terms of service</li></ul>
  <div class="sep" style="left:600px"></div>

  <h6 style="left:663px">ORDER INFORMATION</h6>
  <ul class="col" style="left:668px"><li>My Account</li><li>Shipping Information</li><li>Returns &amp; Exchanges</li></ul>
  <div class="sep" style="left:860px"></div>

  <h6 style="left:915px">CONTACT US</h6>
  <div class="col contact" style="left:915px;line-height:16px">
    <div><svg width="8" height="10" viewBox="0 0 12 16"><path d="M6 0a6 6 0 0 0-6 6c0 4.5 6 10 6 10s6-5.5 6-10a6 6 0 0 0-6-6z" fill="#3fae6a"/></svg><span>Brovalin Solvex, Inc.<br>2217 Meadowline Pkwy. Suite 310<br>Ashford Falls, TX 75990</span></div>
    <div style="margin-top:6px"><svg width="10" height="10" viewBox="0 0 14 14"><path d="M3 1l2.5 3-1.5 1.5c.8 1.8 2.2 3.2 4 4L9.5 8 13 10.5 11.5 13C6 13 1 8 1 2.5z" fill="#3fae6a"/></svg><span>Office: (855) 555-0148</span></div>
    <div style="margin-top:6px"><svg width="10" height="8" viewBox="0 0 10 8"><rect width="10" height="8" fill="#3fae6a"/></svg><span>info@brovalin-solvex.com</span></div>
  </div>
</footer>

<div class="abs bottom">Copyright 2015 Brovalin Solvex™. All Rights Reserved.</div>
<div class="abs social" style="left:1074px;background:var(--green)"></div>
<div class="abs social" style="left:1112px;border:1px solid #888"></div>

</body>
</html>
```